Aunt Ruwaida's Bakery

I am about to create a luxury boutique that specializes in cake baking and cupcake
and ready for parties and special events and order delivery
the logo has already made

Industry/Entity Type

Boutique

Contact Information for Business Card

Email:auntruwaidasbakery@mailvelo.com
Instagram: aunt_ruwaida_bakery
Twitter: xxxxxxx
WhatsApp: xxxxxxx

Requirements
Must have
• luxury design

```html
<!DOCTYPE html>
<html lang="en">
<head>
<meta charset="utf-8">
<title>Aunt Ruwaida's Bakery – Business Card</title>
<link href="https://fonts.googleapis.com/css2?family=Arimo:wght@400;700&display=swap" rel="stylesheet">
<style>
  :root {
    --page-bg: #e9e6e3;
    --card-black: #161616;
    --foil-silver: #9a9a9a;
    --logo-area-dark: #262626;
    --logo-area-light: #3a3a3a;
    --logo-area-pink: #4a3a3f;
    --muted-grey: #8a8a8a;
    --text-white: #f2f2f2;
    --accent-pink: #e8a3b6;
    --shadow: rgba(0,0,0,0.22);
  }
  * { box-sizing: border-box; margin: 0; padding: 0; }
  html, body {
    width: 1200px; height: 787px; overflow: hidden;
    background: var(--page-bg);
    font-family: "Arimo", Arial, sans-serif;
  }
  .sheet {
    width: 1200px; height: 787px;
    display: flex; align-items: center; justify-content: center; gap: 40px;
  }
  .card {
    position: relative;
    width: 540px; height: 309px;
    background: var(--card-black);
    box-shadow: 0 10px 30px var(--shadow);
  }
  .logo-area {
    position: absolute;
    border-radius: 6px;
  }
  /* front */
  .card-front .logo-area {
    left: 160px; top: 50px; width: 220px; height: 150px;
    background: radial-gradient(ellipse at center, var(--logo-area-light), var(--logo-area-dark));
  }
  .card-front .website {
    position: absolute; left: 44px; bottom: 34px;
    color: var(--muted-grey); font-size: 12px; letter-spacing: 3px;
  }
  /* back */
  .card-back .contact {
    position: absolute; left: 34px; top: 72px;
    color: var(--text-white);
  }
  .person-name { color: var(--accent-pink); font-size: 19px; font-weight: 700; }
  .person-role { font-size: 14px; margin-top: 4px; margin-bottom: 14px; }
  .contact-list { list-style: none; }
  .contact-list li {
    display: flex; align-items: center; gap: 10px;
    font-size: 14px; line-height: 1; margin-bottom: 9px;
  }
  .contact-list svg { width: 14px; height: 14px; flex: none; }
  .handle-dot {
    width: 12px; height: 12px; margin: 0 1px; border-radius: 50%;
    background: var(--accent-pink); flex: none;
  }
  .card-back .logo-area {
    right: 26px; top: 98px; width: 190px; height: 130px;
    background: radial-gradient(ellipse at center, var(--logo-area-pink), var(--logo-area-dark));
  }
</style>
</head>
<body>
<main class="sheet">
  <section class="card card-front" aria-label="Card front">
    <div class="logo-area" role="img" aria-label="Silver foil ornamental bakery logo with the Aunt Ruwaida's Bakery name"></div>
    <p class="website">www.auntruwaidasbakery.com</p>
  </section>

  <section class="card card-back" aria-label="Card back">
    <div class="contact">
      <p class="person-name">Samir Halabi</p>
      <p class="person-role">President</p>
      <ul class="contact-list">
        <li>
          <svg viewBox="0 0 16 16" aria-hidden="true"><path fill="var(--accent-pink)" d="M3 1h3l1.5 4-2 1.3a9 9 0 0 0 4.2 4.2L11 8.5l4 1.5v3a2 2 0 0 1-2 2A13 13 0 0 1 1 3a2 2 0 0 1 2-2z"/></svg>
          555 0142 7781
        </li>
        <li>
          <svg viewBox="0 0 16 16" aria-hidden="true"><rect x="1" y="3" width="14" height="10" rx="1" fill="var(--accent-pink)"/><path d="M1.5 3.8 8 9l6.5-5.2" fill="none" stroke="var(--card-black)" stroke-width="1.3"/></svg>
          auntruwaidasbakery@mailvelo.com
        </li>
        <li><span class="handle-dot"></span>auntruwaidasbakery</li>
        <li><span class="handle-dot"></span>aunt_ruwaida_bakery</li>
        <li><span class="handle-dot"></span>auntruwaidasbakery</li>
      </ul>
    </div>
    <div class="logo-area" role="img" aria-label="Grey and pink ornamental bakery logo with the Aunt Ruwaida's Bakery name"></div>
  </section>
</main>
</body>
</html>
```